Business Card Design Project

I have a two letter domain name qo.com.au (lower case font please). I want a business card, cum logo that is die cut (around the qo segment at least) that fits standard business card size.
qo is all about what 'I am' - a journalist, blogger, analyst, commentator. My mantra is "I wander so qo'.
The reverse of the card only needs my name Lon Fitch, email lon@qo.com.au and mobile +61 400 555 817
Target Market(s)
Mainly people that will use my professional writing services and suppliers that will provide product for review
Industry/Entity Type
Business
Requirements
Must have
- One side is qo.com.au (hint - the .com.au can be vertical or horizontal to fit - the qo should be as large as possible).
The other requires large size font name, email and phone details (so no one needs glasses to read it).
The die cut can be just to highlight the qo segment - need not be around the whole card.
Font used in the past was Belwe (old style - very much like the i used in the information symbol).
Colours - no preference - prefer two colour to process colour but can also be an outline font instead of solid colour.

```html
<!DOCTYPE html>
<html lang="en">
<head>
<meta charset="utf-8">
<title>qo.com.au business card</title>
<link rel="stylesheet" href="https://fonts.googleapis.com/css2?family=Cardo:wght@400;700&family=Delius&family=Tinos&display=swap">
<style>
  :root {
    --page: #ffffff;
    --card: #fdc29e;
    --card-shadow: #c9967d;
    --ink-grey: #9c8b77;
    --ink-olive: #6b5a2e;
    --label: #111111;
  }
  html, body {
    margin: 0;
    padding: 0;
    background: var(--page);
    overflow: hidden;
  }
  .sheet {
    display: block;
    width: 1200px;
    height: 396px;
  }
  .card-face { fill: var(--card); }
  .card-edge { fill: var(--card-shadow); }
  .mantra {
    font-family: "Delius", cursive;
    font-size: 26px;
    letter-spacing: 0.16em;
    fill: var(--ink-grey);
  }
  .domain {
    font-family: "Cardo", serif;
    font-weight: 700;
    font-size: 104px;
    letter-spacing: 0.01em;
    fill: var(--ink-grey);
  }
  .holder-name {
    font-family: "Cardo", serif;
    font-size: 42px;
    letter-spacing: 0.04em;
    fill: var(--ink-olive);
  }
  .contact-line {
    font-family: "Cardo", serif;
    font-size: 28px;
    letter-spacing: 0.06em;
    fill: var(--ink-olive);
  }
  .side-label {
    font-family: "Tinos", serif;
    font-size: 21px;
    fill: var(--label);
  }
</style>
</head>
<body>
<svg class="sheet" viewBox="0 0 1200 396" xmlns="http://www.w3.org/2000/svg">
  <g class="card card-front">
    <polygon class="card-edge" points="570,20 583,20 583,333 90,333 72,300 570,300"/>
    <polygon class="card-face" points="72,0 570,0 570,300 72,300 0,152"/>
    <text class="mantra" x="556" y="52" text-anchor="end">I wander so qo</text>
    <text class="domain" x="300" y="205" text-anchor="middle">qo.com.au</text>
  </g>

  <g class="card card-back">
    <polygon class="card-edge" points="616,20 632,20 632,300 1120,300 1104,333 616,333"/>
    <polygon class="card-face" points="632,0 1120,0 1198,150 1120,300 632,300"/>
    <text class="holder-name" x="906" y="88" text-anchor="middle">Lon Fitch</text>
    <text class="contact-line" x="906" y="176" text-anchor="middle">email lon@qo.com.au</text>
    <text class="contact-line" x="912" y="235" text-anchor="middle">mobile +61 400 555 817</text>
  </g>

  <text class="side-label" x="276" y="386" text-anchor="middle">FRONT</text>
  <text class="side-label" x="928" y="383" text-anchor="middle">BACK</text>
</svg>
</body>
</html>
```